Menu: A4 (double sided) Lunch/Dinner Menu (one side) + Pizza Menu (other side)

Hello.
We would like to create a new style of menus.
Must be easy to read - a summer feel, crisp, clean, beachy, possible retro feel, colours probably based on our website colours (see address below).
Simple and casual is best as we are a casual beachside Cafe.
This menu will be double sided therefore this job is 2 pages.
If you win this job we will have 2 or 3 more menus for you to create soon after (Drinks, Breakfast, possibly a small Kids menu).
The paper for these menus we expect will be a nice white paper which will then be matte laminated.
Colours possible are the green colour #3a6066, the terracotta on our website logo border and website buttons, maybe a little yellow but must be easy to read on white paper.
Black for text might be okay if this is your best design option.
Please view our website and take a feel for the business, location, the existing website branding and website colours we are trying to achieve, www.tidelinekitchen.com.au
We prefer to avoid overwhelming the guest with too many colours on the menus (hence the white paper) as the building is so colourful (El Prado, Argentina, inspired) and the guest experience can be complimented via crisp easy to read menus.
IMPORTANT:
The menus provided please must be fully and easily editable by us in the future.
If you win the job, you must please provide clear instructions on how our staff can edit the menus in the future if project is delivered in Adobe format. Word is also an option for us if you like.
As such, we have attached some documents: the 2x Word documents for the text, 2x .pdf so you can see the fonts and style we were using previously (was printing on recycled brown paper then matte laminated).
If you wished to use the SeaLife Font (this is the existing Font for headings) please let us know as we purchased that font and can provide it.
We have also attached a menu from Marlowe Tavern which we feel has a nice retro feel.
Please include our Instagram in 1 place on the menu @tidelinekitchen
Finally, please note,
we never wish to waste anyone's time so we will narrow down the submissions quickly based on first drafts (please know this is because we appreciate your effort and know your time is valuable) and we will then work with the top designer to finalise in a professional fashion.
Thank you.

```html
<!DOCTYPE html>
<html lang="en">
<head>
<meta charset="utf-8">
<title>Lunch + Dinner and Pizza Menus</title>
<link href="https://fonts.googleapis.com/css2?family=Kanit:wght@300;400;500;600&display=swap" rel="stylesheet">
<style>
  :root{
    --sea:#375e64;
    --terracotta:#b4521f;
    --paper:#ffffff;
    --backdrop:#aaaaaa;
    --highlight:#f1e24a;
  }
  *{margin:0;padding:0;box-sizing:border-box}
  html,body{width:1200px;height:862px;overflow:hidden}
  body{background:var(--backdrop);position:relative;font-family:"Kanit",sans-serif;color:var(--sea)}
  .page{position:absolute;top:47px;width:544px;height:769px;background:var(--paper)}
  .page--lunch{left:40px}
  .page--pizza{left:616px}

  .menu-title{position:absolute;left:0;right:0;text-align:center;font-weight:600;letter-spacing:-1px;line-height:1}
  .page--lunch .menu-title{top:27px;font-size:38px}
  .page--pizza .menu-title{top:29px;font-size:40px}
  .legend{position:absolute;left:0;right:0;text-align:center;font-size:8px;font-weight:500}
  .legend .tag{color:var(--terracotta);font-weight:600}
  .page--lunch .legend{top:65px}
  .pizza-sub{position:absolute;top:68px;left:0;right:0;text-align:center;font-size:12px;font-weight:600}
  .page--pizza .legend{top:86px}

  .allergy{position:absolute;top:104px;left:48px;width:448px;text-align:center;font-size:8.3px;font-weight:300;line-height:13.7px}
  .allergy em{font-weight:500;text-decoration:underline;text-decoration-color:var(--highlight);text-decoration-thickness:2px}

  .sides{position:absolute;top:166px;left:54px;width:440px;font-size:12.5px;font-weight:600}
  .sides span{position:absolute;white-space:nowrap}
  .sides b{font-weight:400;margin-left:14px}

  .section{position:absolute;left:54px;width:435px}
  .section-head{display:flex;align-items:baseline;gap:10px;margin-bottom:8px}
  .section-title{font-size:21px;font-weight:500;line-height:1;white-space:nowrap}
  .section-title small{font-size:21px;font-weight:500}
  .section-rule{flex:1;border-bottom:1.5px dotted var(--sea);transform:translateY(-3px)}
  .columns{display:grid;grid-template-columns:182px 214px;column-gap:37px;padding-left:2px}

  .item{margin-bottom:9px}
  .item-head{display:flex;justify-content:space-between;align-items:flex-start;gap:6px}
  .item-name{font-size:12px;font-weight:600;line-height:11px;letter-spacing:-.1px;margin-bottom:1px}
  .qty{font-size:8px;font-weight:600}
  .tag{color:var(--terracotta);font-size:8px;font-weight:600}
  .price{font-size:12px;font-weight:400;line-height:11px}
  .item-desc{font-size:8.3px;font-weight:500;line-height:10px}
  .item-desc small{font-size:6.5px}
  .item-extra{font-size:6.5px;font-weight:500;line-height:10px}
  .pizza .item{margin-bottom:11px}
  .pizza .item-desc{line-height:11px}
  .chili{width:8px;height:8px;vertical-align:-1px;fill:var(--terracotta)}

  .platter-desc{font-size:8.3px;font-weight:500;line-height:11px;padding-left:2px;margin-bottom:9px}
  .choose{display:flex;gap:6px;margin:6px 0 18px;font-size:8px;font-weight:500;line-height:10px}
  .choose-label{color:var(--terracotta)}
  .choose .note{font-size:6.5px}
  .lunch-bottom .columns > div:last-child .item{margin-bottom:8px}
</style>
</head>
<body>

<section class="page page--lunch" aria-label="Lunch and dinner menu">
  <h1 class="menu-title">LUNCH + DINNER</h1>
  <p class="legend"><span class="tag">V</span> – VEGETARIAN &nbsp; / &nbsp; <span class="tag">GFO</span> – GLUTEN FRIENDLY OPTIONAL, PLEASE ASK</p>

  <div class="section" style="top:103px">
    <div class="section-head"><h2 class="section-title">ENTREE</h2><span class="section-rule"></span></div>
    <div class="columns">
      <div>
        <div class="item"><div class="item-head"><h3 class="item-name">GARLIC BREAD <span class="qty">( 2 )</span> <span class="tag">V</span></h3><span class="price">8</span></div></div>
        <div class="item" style="margin-top:-1px"><div class="item-head"><h3 class="item-name">SALT &amp; PEPPER SQUID</h3><span class="price">18</span></div><p class="item-desc">W/ THAI DIPPING SAUCE</p></div>
        <div class="item"><div class="item-head"><h3 class="item-name">DUO OF DIP <span class="tag">V</span></h3><span class="price">14</span></div><p class="item-desc">W/ PITA</p></div>
        <div class="item"><div class="item-head"><h3 class="item-name">BOWL OF CHIPS <span class="tag">V</span></h3><span class="price">11</span></div><p class="item-desc">W/ TOMATO SAUCE</p></div>
        <div class="item"><div class="item-head"><h3 class="item-name">SEASONED WEDGES <span class="tag">V</span></h3><span class="price">15</span></div><p class="item-desc">W/ SOUR CREAM &amp; SWEET CHILLI</p></div>
      </div>
      <div>
        <div class="item"><div class="item-head"><h3 class="item-name">ONION RINGS <span class="qty">( 12 )</span> <span class="tag">V</span></h3><span class="price">13</span></div><p class="item-desc">BEER BATTERED W/ TANGY MAYO</p></div>
        <div class="item"><div class="item-head"><h3 class="item-name">VIETNAMESE SPRING ROLLS <span class="qty">( 3 )</span></h3><span class="price">11</span></div><p class="item-desc">CHICKEN, HOME-MADE</p></div>
        <div class="item"><div class="item-head"><h3 class="item-name">BRUSCHETTA <span class="qty">( 1 )</span> <span class="tag">V</span></h3><span class="price">10</span></div><p class="item-desc">W/ OLIVE OIL, TOMATO &amp; RED ONION SALSA,<br>BALSAMIC GLAZE, FETA</p></div>
      </div>
    </div>
  </div>

  <div class="section" style="top:294px">
    <div class="section-head"><h2 class="section-title">MAINS</h2><span class="section-rule"></span></div>
    <div class="columns">
      <div>
        <div class="item"><div class="item-head"><h3 class="item-name">THE FISH &amp; CHIPS</h3><span class="price">25</span></div><p class="item-desc">HOUSE-CRUMBED BUTTERFISH<br>W/ CHIPS, TARTARE &amp; SIDE SALAD</p></div>
        <div class="item"><div class="item-head"><h3 class="item-name">SMOKEY BEEF &amp; BACON<br>CHEESE BURGER</h3><span class="price">23</span></div><p class="item-desc">W/ CHIPS, ONION RINGS, GERKINS<br>&amp; TANGY MAYO</p><p class="item-extra">+ JALAPENOS 2<br>+ PINEAPPLE 2</p></div>
        <div class="item"><div class="item-head"><h3 class="item-name">SALT &amp; PEPPER SQUID</h3><span class="price">31</span></div><p class="item-desc">GOLDEN TANGLES W/ CHIPS,<br>THAI DIPPING SAUCE &amp; SIDE SALAD</p></div>
      </div>
      <div>
        <div class="item"><div class="item-head"><h3 class="item-name">SEAFOOD BASKET</h3><span class="price">31</span></div><p class="item-desc">CRUMBED BUTTERFISH, GRILLED<br>PRAWNS, SALT &amp; PEPPER SQUID,<br>CHIPS, TARTARE &amp; SIDE SALAD</p></div>
        <div class="item"><div class="item-head"><h3 class="item-name">ATLANTIC SALMON</h3><span class="price">31</span></div><p class="item-desc">SERVED W/ MASH, TERIYAKI SAUCE<br>&amp; WINTER VEGETABLES <small>( CONTAINS BREADCRUMBS )</small></p></div>
        <div class="item"><div class="item-head"><h3 class="item-name">CHICKEN PARMIGIANA</h3><span class="price">27</span></div><p class="item-desc">HOUSE-CRUMBED BREAST SCHNITZEL,<br>NAPOLI SAUCE, MOZZARELLA,<br>CHIPS &amp; SIDE SALAD</p><p class="item-extra">+ BACON AND PINEAPPLE 4<br>+ JALAPENOS AND PINEAPPLE 4</p></div>
      </div>
    </div>
  </div>

  <div class="section lunch-bottom" style="top:505px">
    <div class="section-head"><h2 class="section-title">SALTWATER PLATTER <small>for 2</small></h2><span class="section-rule"></span></div>
    <p class="platter-desc">BEER BATTERED FLATHEAD, SALT &amp; PEPPER SQUID, PRAWN SKEWERS, GRILLED CHICKEN, LAMB &amp;<br>CHORIZO, SERVED WITH ANTIPASTO, DIPPING SAUCES, PITA &amp; GARLIC BREAD 90 (+45 PP)</p>
    <div class="columns">
      <div>
        <div class="item"><div class="item-head"><h3 class="item-name">NEW YORK SIRLOIN <span class="tag">GFO</span></h3><span class="price">38</span></div><p class="item-desc">400G MSA W/ MASH &amp; WINTER<br>VEGETABLES</p>
          <div class="choose"><span class="choose-label">CHOOSE:</span><span>MUSHROOM GRAVY<br>/ CLASSIC GRAVY<br>/ SURF ‘N’ TURF <span class="tag" style="font-size:8px">GFO</span> +6<br><span class="note">PLEASE ALLOW 35+ MINUTES<br>FOR "WELL-DONE"</span></span></div>
        </div>
        <div class="item"><div class="item-head"><h3 class="item-name">CHICKEN CAESAR</h3><span class="price">27</span></div><p class="item-desc">W/ BACON, ANCHOVIES, EGG,<br>CAESAR DRESSING, PARMESAN,<br>SPANISH ONION, GARLIC BREAD</p></div>
      </div>
      <div>
        <div class="item"><div class="item-head"><h3 class="item-name">LAMB SALAD <span class="tag">GFO</span></h3><span class="price">30</span></div><p class="item-desc">SKEWERS W/ TRADITIONAL GREEK<br>SALAD, TZATZIKI &amp; GARLIC BREAD</p><p class="item-extra">+ EXTRA LAMB 8</p></div>
        <div class="item"><div class="item-head"><h3 class="item-name">THAI CHICKEN CURRY <svg class="chili" viewBox="0 0 10 10" aria-hidden="true"><path d="M1 9.5C4 9 7.5 6 8 2.5L9.5 1 8.6.6 7.2 2C5 4 3 7 1 9.5Z"/></svg><span class="tag"> MILD GFO</span></h3><span class="price">26</span></div><p class="item-desc">TRADITIONAL RECIPE, W/ JASMINE RICE<br>&amp; PAPADUMS</p></div>
        <div class="item"><div class="item-head"><h3 class="item-name">BEACH BURGER <span class="tag">V</span></h3><span class="price">23</span></div><p class="item-desc">HOUSE-MADE PEA &amp; CORN RICOTTA<br>FRITTER, PINEAPPLE, W/ WEDGES,<br>ONION RINGS, SWEET CHILLI</p></div>
        <div class="item"><div class="item-head"><h3 class="item-name">VEGAN CURRY <svg class="chili" viewBox="0 0 10 10" aria-hidden="true"><path d="M1 9.5C4 9 7.5 6 8 2.5L9.5 1 8.6.6 7.2 2C5 4 3 7 1 9.5Z"/></svg><span class="tag"> MILD GFO / V</span></h3><span class="price">24</span></div><p class="item-desc">CHICKPEA &amp; PUMPKIN W/ FRESH TOMATOES<br>&amp; BASIL, JASMINE RICE &amp; PAPADUMS</p></div>
      </div>
    </div>
  </div>
</section>

<section class="page page--pizza pizza" aria-label="Pizza menu">
  <h1 class="menu-title">PIZZA</h1>
  <p class="pizza-sub">ALL 12” WITH HOUSE-MADE TOMATO BASE &amp; MOZZARELLA</p>
  <p class="legend"><span class="tag">V</span> – VEGETARIAN GLUTEN FREE BASE +$4 VEGAN CHEESE +$3</p>
  <p class="allergy"><em>Allergies? Please let us know!</em> &nbsp;All care is taken to cater for allergies including gluten, however our kitchen is small and we do not have separate preparation or cooking areas. As such, there is risk of cross-contact with your allergen and we are unable to guarantee allergen-free meals. Olives may very rarely contain pips.</p>

  <div class="sides">
    <span style="left:0">GARLIC BREAD<b>8</b></span>
    <span style="left:162px">GREEK SALAD<b>16</b></span>
    <span style="left:313px">GARDEN SALAD<b>12</b></span>
  </div>

  <div class="section" style="top:199px">
    <div class="section-head"><h2 class="section-title">STANDARD</h2><span class="section-rule"></span></div>
    <div class="columns">
      <div>
        <div class="item"><div class="item-head"><h3 class="item-name">HAWAIIAN</h3><span class="price">22</span></div><p class="item-desc">HAM, PINEAPPLE</p></div>
        <div class="item"><div class="item-head"><h3 class="item-name">MARGHERITA <span class="tag">V</span></h3><span class="price">22</span></div><p class="item-desc">MARINATED &amp; DICED TOMATOES,<br>FRESH BASIL</p></div>
        <div class="item"><div class="item-head"><h3 class="item-name">BBQ CHICKEN</h3><span class="price">26</span></div><p class="item-desc">CHICKEN, SALAMI, TOMATO,<br>SPANISH ONION, BBQ SAUCE</p></div>
        <div class="item"><div class="item-head"><h3 class="item-name">CHORIZO</h3><span class="price">26</span></div><p class="item-desc">CHORIZO, SALAMI, TOMATO,<br>MUSHROOMS, SPANISH ONION <svg class="chili" viewBox="0 0 10 10" aria-hidden="true"><path d="M1 9.5C4 9 7.5 6 8 2.5L9.5 1 8.6.6 7.2 2C5 4 3 7 1 9.5Z"/></svg></p></div>
        <div class="item"><div class="item-head"><h3 class="item-name">SALTWATER SPECIAL</h3><span class="price">26</span></div><p class="item-desc">HAM, SALAMI, PRAWNS,<br>KALAMATA OLIVES, ROASTED<br>CAPSICUM, MUSHROOMS,<br>SPANISH ONION</p></div>
        <div class="item"><div class="item-head"><h3 class="item-name">MEAT LOVERS</h3><span class="price">26</span></div><p class="item-desc">CHICKEN, BACON, SALAMI,<br>HAM, BBQ SAUCE</p></div>
      </div>
      <div>
        <div class="item"><div class="item-head"><h3 class="item-name">MONA LISA</h3><span class="price">26</span></div><p class="item-desc">CHICKEN, PINEAPPLE, HAM,<br>SPANISH ONION, MUSHROOMS</p></div>
        <div class="item"><div class="item-head"><h3 class="item-name">PUTTANESCA</h3><span class="price">26</span></div><p class="item-desc">ANCHOVIES, CAPERS, SALAMI,<br>KALAMATA OLIVES,<br>ROASTED CAPSICUM, PARMESAN</p></div>
        <div class="item"><div class="item-head"><h3 class="item-name">TROPICAL CHICKEN</h3><span class="price">26</span></div><p class="item-desc">CHICKEN, PINEAPPLE, SPANISH ONION,<br>CHILLI, TOMATO, MUSHROOMS <svg class="chili" viewBox="0 0 10 10" aria-hidden="true"><path d="M1 9.5C4 9 7.5 6 8 2.5L9.5 1 8.6.6 7.2 2C5 4 3 7 1 9.5Z"/></svg></p></div>
        <div class="item"><div class="item-head"><h3 class="item-name">VEGETARIAN <span class="tag">V</span></h3><span class="price">26</span></div><p class="item-desc">ROASTED CAPSICUM, TOMATO,<br>MUSHROOMS, ARTICHOKES,<br>KALAMATA OLIVES, SPANISH ONION</p></div>
        <div class="item"><div class="item-head"><h3 class="item-name">BUILD YOUR OWN <span class="tag">V</span></h3><span class="price">26</span></div><p class="item-desc">TOMATO BASE, MOZZARELLA<br>&amp; FOUR TOPPINGS</p></div>
      </div>
    </div>
  </div>

  <div class="section" style="top:523px">
    <div class="section-head"><h2 class="section-title">GOURMET</h2><span class="section-rule"></span></div>
    <div class="columns">
      <div>
        <div class="item"><div class="item-head"><h3 class="item-name">CAVEMAN</h3><span class="price">29</span></div><p class="item-desc">CHICKEN, LAMB, PORK SAUSAGE,<br>CHORIZO, SALAMI, BACON,<br>SPANISH ONION, CARAMELISED<br>ONION, SMOKEY BBQ SAUCE</p></div>
        <div class="item"><div class="item-head"><h3 class="item-name">SPICY PRAWN &amp;<br>BASIL PESTO</h3><span class="price">29</span></div><p class="item-desc">PRAWNS, ROASTED CAPSICUM,<br>CHILLI, SPRING ONION, BASIL PESTO <svg class="chili" viewBox="0 0 10 10" aria-hidden="true"><path d="M1 9.5C4 9 7.5 6 8 2.5L9.5 1 8.6.6 7.2 2C5 4 3 7 1 9.5Z"/></svg></p></div>
        <div class="item"><div class="item-head"><h3 class="item-name">GOURMET VEGETARIAN <span class="tag">V</span></h3><span class="price">29</span></div><p class="item-desc">PUMPKIN, EGGPLANT,<br>SEMI-DRIED TOMATOES, ROASTED<br>CAPSICUM, RED ONION, BULGARIAN<br>FETA, KALAMATA OLIVES, SPINACH</p></div>
      </div>
      <div>
        <div class="item"><div class="item-head"><h3 class="item-name">RUSTY BANJO</h3><span class="price">29</span></div><p class="item-desc">CHILLI JAM, JALAPENO PEPPERS,<br>MUSHROOMS, BACON, CHILLI,<br>CHORIZO, SPANISH ONION <svg class="chili" viewBox="0 0 10 10" aria-hidden="true"><path d="M1 9.5C4 9 7.5 6 8 2.5L9.5 1 8.6.6 7.2 2C5 4 3 7 1 9.5Z"/></svg><svg class="chili" viewBox="0 0 10 10" aria-hidden="true"><path d="M1 9.5C4 9 7.5 6 8 2.5L9.5 1 8.6.6 7.2 2C5 4 3 7 1 9.5Z"/></svg></p></div>
        <div class="item"><div class="item-head"><h3 class="item-name">LAMB PIZZA</h3><span class="price">29</span></div><p class="item-desc">LAMB, RED ONION, FRESH TOMATO,<br>TZATZIKI, SPRING ONION</p></div>
        <div class="item"><div class="item-head"><h3 class="item-name">LOS POLLOS</h3><span class="price">29</span></div><p class="item-desc">CHICKEN, PUMPKIN, BASIL PESTO,<br>SPINACH, FETA, PINE NUTS</p></div>
        <div class="item"><div class="item-head"><h3 class="item-name">SEAFOOD PIZZA</h3><span class="price">29</span></div><p class="item-desc">ARRAY OF SEAFOOD</p></div>
      </div>
    </div>
  </div>
</section>

</body>
</html>
```